Flyer Design Project - law firm

I need a design for an advertising flyer for my law firm.
Ideally the size of the document will be one page A4.
I have attached a copy of the logo. I would like the lettering for 'Dornwick Legal' to be all the same size, rather than the 'S' and 'L' being slightly larger
The flyer must include the text below:
Wills
Anyone who owns property or investments or has family obligations should have a Will to ensure that their assets are distributed in accordance with their wishes and that their children are cared for by the guardians of their choosing. Without a Will, these vital decisions are determined by the government or the courts of the State or Territory which you lived in at the time of your death.
Dornwick Legal can assist you in the preparation of a legal will tailored to your particular circumstances to ensure that your wishes are followed.
We are offering Halbrook- Crestmere clients a free discussion of their will requirements and a heavily discounted standard wills package of
$330.00* for a single will
$550.00* for couples wills
These prices are only valid prior to your conveyancing settlement for standard wills (e.g. not including a testamentary trust or other complications.
Please contact us on or provide Halbrook Crestmere with authority for us to contact you today.
Updates
Hi All,
I have posted a copy of the proposed logo. Please note that I need the wording of 'Dornwick Legal' to all be the same size, rather than the 'S' and 'L' being slightly larger.
If you require anything further please let me know.
Thanks
I have added copies of the logo in ups format,
If you require anything further please let know.
Thanks for your assistance.
Industry/Entity Type
Advertising
Look and feel
Each slider illustrates characteristics of the customer's brand and the style your logo design should communicate.

```html
<!DOCTYPE html>
<html lang="en">
<head>
<meta charset="utf-8">
<title>Dornwick Legal – Wills Flyer</title>
<link rel="stylesheet" href="https://fonts.googleapis.com/css2?family=Archivo+Narrow:ital,wght@0,400;0,600;1,400;1,600&family=Marcellus&display=swap">
<style>
  :root {
    --parchment-light: #f7ecb5;
    --parchment-mid: #ecd98e;
    --parchment-deep: #d9bd6c;
    --orange: #f26b1d;
    --orange-soft: rgba(242, 107, 29, 0.45);
    --ink: #1d1a14;
  }
  html, body { margin: 0; padding: 0; overflow: hidden; }
  body { width: 848px; height: 1200px; }
  .flyer {
    position: relative;
    width: 848px;
    height: 1200px;
    overflow: hidden;
    font-family: "Archivo Narrow", "Arial Narrow", sans-serif;
    color: var(--ink);
  }
  .flyer-backdrop {
    position: absolute; inset: 0;
    background:
      radial-gradient(ellipse at 30% 25%, var(--parchment-light) 0%, rgba(247,236,181,0) 60%),
      radial-gradient(ellipse at 75% 70%, var(--parchment-deep) 0%, rgba(217,189,108,0) 55%),
      linear-gradient(160deg, var(--parchment-light) 0%, var(--parchment-mid) 55%, var(--parchment-deep) 100%);
  }
  .family-silhouette {
    position: absolute; left: 560px; top: 880px; width: 288px; height: 320px;
    background: radial-gradient(ellipse at 50% 70%, rgba(176,140,60,0.75) 0%, rgba(176,140,60,0) 70%);
  }
  .border-band { position: absolute; background: var(--orange-soft); }
  .band-top-left { left: 8px; top: 9px; width: 160px; height: 12px; }
  .band-top-mid { left: 258px; top: 9px; width: 340px; height: 12px; }
  .band-bottom { left: 8px; top: 1179px; width: 832px; height: 12px; }
  .band-left { left: 9px; top: 24px; width: 12px; height: 1152px; }
  .band-right { left: 817px; top: 9px; width: 12px; height: 1167px; }
  .ruled-sheet { position: absolute; left: 0; top: 0; }
  .brand {
    position: absolute; left: 146px; top: 28px;
    display: flex; align-items: center; gap: 24px;
  }
  .brand-dot {
    width: 112px; height: 112px; border-radius: 50%;
    background: var(--orange);
  }
  .brand-name {
    font-family: "Marcellus", serif;
    font-size: 44px; letter-spacing: 2px;
    color: var(--ink); text-transform: uppercase;
  }
  .section-title {
    position: absolute; left: 104px; top: 178px; margin: 0;
    font-size: 22px; font-weight: 600; line-height: 30px;
  }
  .body-copy {
    position: absolute; left: 104px; width: 620px;
    margin: 0; font-size: 19.2px; line-height: 34px;
    text-align: justify; text-align-last: left;
  }
  .copy-intro { top: 219px; }
  .copy-service { top: 423px; }
  .copy-offer { top: 525px; }
  .price {
    position: absolute; left: 384px;
    display: flex; align-items: center; gap: 14px;
    font-style: italic; font-weight: 600; font-size: 18px;
  }
  .price-one { top: 634px; }
  .price-two { top: 703px; }
  .price-arrow { width: 16px; height: 26px; }
  .price-amount { margin-right: 10px; }
  .copy-terms { position: absolute; left: 98px; top: 771px; width: 630px; margin: 0; font-size: 18.8px; line-height: 34px; }
  .call-to-action {
    position: absolute; left: 215px; width: 400px; top: 911px;
    margin: 0; text-align: center;
    font-weight: 600; font-size: 20px; line-height: 34.5px;
  }
  .contact-line {
    position: absolute; left: 115px; width: 600px; margin: 0;
    text-align: center; font-style: italic; font-size: 16px;
  }
  .contact-email { top: 1090px; }
  .contact-directions { top: 1125px; }
</style>
</head>
<body>
<main class="flyer">
  <div class="flyer-backdrop" role="img" aria-label="Soft textured parchment background"></div>
  <div class="family-silhouette" role="img" aria-label="Faint silhouette of a family standing together"></div>

  <div class="border-band band-top-left" role="img" aria-label="Decorative border band"></div>
  <div class="border-band band-top-mid" role="img" aria-label="Decorative border band"></div>
  <div class="border-band band-bottom" role="img" aria-label="Decorative border band"></div>
  <div class="border-band band-left" role="img" aria-label="Decorative border band"></div>
  <div class="border-band band-right" role="img" aria-label="Decorative border band"></div>

  <svg class="ruled-sheet" width="848" height="1200" viewBox="0 0 848 1200" aria-hidden="true">
    <rect x="90" y="143" width="650" height="1003" fill="rgba(255,252,235,0.22)" stroke="rgba(120,110,80,0.35)" stroke-width="2"/>
    <g stroke="rgba(120,110,80,0.28)" stroke-width="2">
      <line x1="90" y1="177" x2="740" y2="177"/><line x1="90" y1="211" x2="740" y2="211"/>
      <line x1="90" y1="245" x2="740" y2="245"/><line x1="90" y1="279" x2="740" y2="279"/>
      <line x1="90" y1="313" x2="740" y2="313"/><line x1="90" y1="347" x2="740" y2="347"/>
      <line x1="90" y1="381" x2="740" y2="381"/><line x1="90" y1="415" x2="740" y2="415"/>
      <line x1="90" y1="449" x2="740" y2="449"/><line x1="90" y1="483" x2="740" y2="483"/>
      <line x1="90" y1="517" x2="740" y2="517"/><line x1="90" y1="551" x2="740" y2="551"/>
      <line x1="90" y1="585" x2="740" y2="585"/><line x1="90" y1="619" x2="740" y2="619"/>
      <line x1="90" y1="653" x2="740" y2="653"/><line x1="90" y1="687" x2="740" y2="687"/>
      <line x1="90" y1="721" x2="740" y2="721"/><line x1="90" y1="755" x2="740" y2="755"/>
      <line x1="90" y1="789" x2="740" y2="789"/><line x1="90" y1="823" x2="740" y2="823"/>
      <line x1="90" y1="857" x2="740" y2="857"/><line x1="90" y1="891" x2="740" y2="891"/>
      <line x1="90" y1="925" x2="740" y2="925"/><line x1="90" y1="959" x2="740" y2="959"/>
      <line x1="90" y1="993" x2="740" y2="993"/><line x1="90" y1="1027" x2="740" y2="1027"/>
      <line x1="90" y1="1061" x2="740" y2="1061"/><line x1="90" y1="1095" x2="740" y2="1095"/>
      <line x1="90" y1="1129" x2="740" y2="1129"/>
    </g>
    <g font-family="Archivo Narrow, sans-serif" font-size="9" fill="rgba(110,100,70,0.55)" text-anchor="middle">
      <text x="76" y="147">1</text><text x="76" y="181">2</text><text x="76" y="215">3</text><text x="76" y="249">4</text><text x="76" y="283">5</text><text x="76" y="317">6</text><text x="76" y="351">7</text><text x="76" y="385">8</text><text x="76" y="419">9</text><text x="76" y="453">10</text><text x="76" y="491">11</text><text x="76" y="525">12</text><text x="76" y="559">13</text><text x="76" y="593">14</text><text x="76" y="627">15</text><text x="76" y="661">16</text><text x="76" y="695">17</text><text x="76" y="729">18</text><text x="76" y="763">19</text><text x="76" y="797">20</text><text x="76" y="831">21</text><text x="76" y="865">22</text><text x="76" y="899">23</text><text x="76" y="937">24</text><text x="76" y="971">25</text><text x="76" y="1005">26</text><text x="76" y="1039">27</text><text x="76" y="1073">28</text><text x="76" y="1107">29</text><text x="76" y="1141">30</text>
      <text x="754" y="147">1</text><text x="754" y="181">2</text><text x="754" y="215">3</text><text x="754" y="249">4</text><text x="754" y="283">5</text><text x="754" y="317">6</text><text x="754" y="351">7</text><text x="754" y="385">8</text><text x="754" y="419">9</text><text x="754" y="453">10</text><text x="754" y="491">11</text><text x="754" y="525">12</text><text x="754" y="559">13</text><text x="754" y="593">14</text><text x="754" y="627">15</text><text x="754" y="661">16</text><text x="754" y="695">17</text><text x="754" y="729">18</text><text x="754" y="763">19</text><text x="754" y="797">20</text><text x="754" y="831">21</text><text x="754" y="865">22</text><text x="754" y="899">23</text><text x="754" y="937">24</text><text x="754" y="971">25</text><text x="754" y="1005">26</text><text x="754" y="1039">27</text><text x="754" y="1073">28</text><text x="754" y="1107">29</text><text x="754" y="1141">30</text>
    </g>
  </svg>

  <header class="brand">
    <span class="brand-dot" aria-hidden="true"></span>
    <span class="brand-name">Dornwick Legal</span>
  </header>

  <h1 class="section-title">Wills</h1>

  <p class="body-copy copy-intro">Anyone who owns property or investments or has family obligations should have a Will to ensure that their assets are distributed in accordance with their wishes and that their children are cared for by the guardians of their choosing. Without a Will, these vital decisions are determined by the government or the courts of the State or Territory which you lived in at the time of your death.</p>

  <p class="body-copy copy-service">Dornwick Legal can assist you in the preparation of a legal will tailored to your particular circumstances to ensure that your wishes are followed.</p>

  <p class="body-copy copy-offer">We are offering Halbrook- Crestmere clients a free discussion of their will requirements and a heavily discounted standard wills package of :</p>

  <div class="price price-one">
    <svg class="price-arrow" viewBox="0 0 16 26" aria-hidden="true"><polygon points="0,0 16,13 0,26" fill="#f26b1d"/></svg>
    <span><span class="price-amount">$330.00</span> for a single will</span>
  </div>
  <div class="price price-two">
    <svg class="price-arrow" viewBox="0 0 16 26" aria-hidden="true"><polygon points="0,0 16,13 0,26" fill="#f26b1d"/></svg>
    <span><span class="price-amount">$550.00</span> for couples wills</span>
  </div>

  <p class="copy-terms">These prices are only valid prior to your conveyancing settlement for standard wills (e.g. not including a testamentary trust or other complications).</p>

  <p class="call-to-action">Please contact us on<br>or provide Halbrook Crestmere<br>with authority for us<br>to contact you today.</p>

  <p class="contact-line contact-email">E-mail: Dornwick Legal@example.com / Phone number: 555 01 234</p>
  <p class="contact-line contact-directions">Directions: Dornwick Legal home example</p>
</main>
</body>
</html>
```